Header/Logo Redesign

****WE HAVE FOUND THE DESIGNER WHO WILL BE HANDLING THIS PROJECT. PLEASE DONT SUBMIT ANY MORE DESIGNS.****
We have been working with a Web/Logo Designer on a new header and logo for our site. We like some of it, but other things need changing.
Overall Look: We are looking for something that is professional, yet still fresh. Most business two business websites seem old fashinoned. The site we like most is www.tallyhaven.com.
Header Thoughts:
-We like the color at the top of the header. The light purple on the menu bar is a little dull though. It seems to be grayed out too much. Notice the pop that www.tallyhaven.com has. We need that pop.
-The fonts on the menu bar don't pop either. I don't know if it is because the font is bad or the thickness of the font is bad or what.
-We are not sold on the green color in the logo and header. It is pretty good, but maybe we can test other colors?
Logo Thoughts:
-I am not sold on the green color. It is pretty good, but maybe test it out with some other colors?
-The logo does not pop like the www.tallyhaven.com logo pops.
-We had started thinking about doing an owl as part of our name/logo or maybe some other type of animal. Look at the ideas I had sent our original graphic designer.
A. http://markvista.net/gallery/detail/842907 - i like that is simple, a little abstract, but I don't like that it is sort of evil.
B. http://markvista.net/gallery/detail/27514 - i like that is abstract.
C. http://pixelbrook.files.quillsite.net/2012/05/torvane4.jpg - i like the slightly abstract.
D. http://sketchlark.net/shots/718204-O-W-L - good - abrstract and slightly turned.
Target Market(s)
Sales and Marketing People - primarily a masculine audience in their 20s to 40s.
Industry/Entity Type
Business
Look and feel

```html
<!DOCTYPE html>
<html lang="en">
<head>
<meta charset="utf-8">
<title>Scoutline – Header</title>
<link rel="stylesheet" href="https://fonts.googleapis.com/css2?family=Noticia+Text:wght@400;700&display=swap">
<style>
  :root {
    --header-top: #3b3b78;
    --header-bottom: #2e2e62;
    --nav-bg: #7474c1;
    --nav-divider: #6363ad;
    --nav-divider-light: #8484cc;
    --panel-bg: #2f2f58;
    --text-light: #ffffff;
    --input-bg: #ffffff;
    --input-border: #c9c9d6;
    --placeholder: #9a9aa6;
    --link: #8f8fe0;
    --green-top: #7cc62a;
    --green-bottom: #4f960f;
    --page-bg: #ffffff;
  }
  * { box-sizing: border-box; margin: 0; padding: 0; }
  html, body {
    width: 1200px; height: 514px; overflow: hidden;
    background: var(--page-bg);
    font-family: "Noticia Text", Georgia, serif;
  }
  .site-header {
    position: absolute; left: 0; top: 0; width: 1200px; height: 89px;
    background: linear-gradient(to bottom, var(--header-top), var(--header-bottom));
  }
  .brand {
    position: absolute; left: 171px; top: 18px;
    display: flex; align-items: center; gap: 10px;
    color: var(--text-light); font-weight: 700; font-size: 40px; letter-spacing: 1px;
  }
  .brand-mark {
    width: 14px; height: 14px; border-radius: 50%; background: var(--text-light);
  }
  .search {
    position: absolute; left: 807px; top: 31px; width: 204px; height: 29px;
    background: var(--input-bg); border: 1px solid var(--input-border); border-radius: 7px;
    box-shadow: inset 0 1px 2px rgba(0,0,0,.15);
    font-family: Arial, sans-serif; font-size: 11px; color: var(--placeholder);
    padding: 7px 14px;
  }
  .search svg { position: absolute; right: 12px; top: 8px; }
  .main-nav {
    position: absolute; left: 0; top: 89px; width: 1200px; height: 50px;
    background: var(--nav-bg);
  }
  .nav-item {
    position: absolute; top: 0; height: 50px; line-height: 50px;
    color: var(--text-light); font-size: 12.5px; letter-spacing: 1px; text-transform: uppercase;
  }
  .nav-divider {
    position: absolute; top: 14px; width: 1px; height: 24px;
    background: var(--nav-divider); box-shadow: 1px 0 0 var(--nav-divider-light);
  }
  .login-tab {
    position: absolute; left: 771px; top: 92px; width: 141px; height: 48px;
    background: var(--panel-bg); border-radius: 6px 6px 0 0;
    color: var(--text-light); font-size: 12.5px; letter-spacing: 1px;
    text-align: center; line-height: 46px; text-transform: uppercase;
  }
  .login-panel {
    position: absolute; left: 771px; top: 139px; width: 184px; height: 155px;
    background: var(--panel-bg); border-radius: 0 6px 6px 6px;
  }
  .field {
    position: absolute; left: 15px; width: 150px; height: 27px;
    background: var(--input-bg); border: 1px solid var(--input-border); border-radius: 10px;
    box-shadow: inset 0 1px 3px rgba(0,0,0,.2);
    font-family: Arial, sans-serif; font-size: 10.5px; color: var(--placeholder);
    padding: 6px 11px;
  }
  .field-user { top: 15px; }
  .field-pass { top: 52px; }
  .remember {
    position: absolute; left: 16px; top: 92px; display: flex; align-items: center; gap: 7px;
    font-family: Arial, sans-serif; font-size: 10.5px; color: var(--link); text-decoration: underline;
  }
  .checkbox {
    width: 13px; height: 13px; background: #e6e6ee; border-radius: 2px; display: block;
  }
  .submit {
    position: absolute; left: 13px; top: 117px; width: 75px; height: 27px;
    background: linear-gradient(to bottom, var(--green-top), var(--green-bottom));
    border-radius: 6px; box-shadow: 0 2px 2px rgba(0,0,0,.35);
    color: var(--text-light); font-weight: 700; font-size: 12px;
    text-align: center; line-height: 27px;
  }
</style>
</head>
<body>
  <header class="site-header">
    <div class="brand"><span class="brand-mark"></span>Scoutline</div>
    <div class="search">Search
      <svg width="11" height="11" viewBox="0 0 11 11"><circle cx="4.5" cy="4.5" r="3.3" fill="none" stroke="#a5a5ad" stroke-width="1.6"/><line x1="7" y1="7" x2="10" y2="10" stroke="#a5a5ad" stroke-width="2"/></svg>
    </div>
  </header>

  <nav class="main-nav">
    <span class="nav-item" style="left:193px">New</span>
    <span class="nav-divider" style="left:243px"></span>
    <span class="nav-item" style="left:264px">People</span>
    <span class="nav-divider" style="left:333px"></span>
    <span class="nav-item" style="left:351px">Companies</span>
    <span class="nav-divider" style="left:447px"></span>
    <span class="nav-item" style="left:463px">Downloads</span>
    <span class="nav-divider" style="left:564px"></span>
    <span class="nav-item" style="left:933px">Free Signup</span>
  </nav>

  <div class="login-tab">Account Login</div>
  <form class="login-panel">
    <div class="field field-user">Username</div>
    <div class="field field-pass">*********</div>
    <label class="remember">
      <svg class="checkbox" viewBox="0 0 13 13"><rect width="13" height="13" rx="2" fill="#e6e6ee"/><path d="M3 6.5l2.5 2.5L10 3.8" fill="none" stroke="#4a4a5a" stroke-width="1.8"/></svg>
      Remember me
    </label>
    <div class="submit">Submit</div>
  </form>
</body>
</html>
```